Design a colorful and bold graphic for the side of my boat

Looking for bold and/or colorful options.
Must include boat name - Keep calm cast on
Boat belongs to me and my daughter - funny, fun loving and enjoy outdoors. We use it for fishing in Texas.
We are close to the same height (she is a teenager). Like something funny/punchy/sassy. Do not want anything sexy.
Would like to end up doing a vinyl print of it to adhere to both sides of boat. Needs to be narrow and long. I will remove the wording currently on the side of the boat that says gullmark boats.

The new graphic kind of sits at two different levels. The top level and then the boat notches in about an inch down to the next one.

Hello designers! Thank you for considering my project. Im looking for a fun energy design to go on the side of my boat and feature the boat name and fish.
Name - Keep Calm Cast On. Used by - my daughter and I - both females and close to the same height. I do not want the image to be sexy in any way. Would love it to show a great image of a fish or us both catching fish. We wear ballcaps with ponytails. The image does not have to contain us but certainly can. Must have fish and boat name though. I like colorful and bold designs. No not care for childish images. I do like edgy, bold, funny, eye catching. etc. My daughter and I are both funny and fun loving and love the water and fishing. Would love to have a cool graphic that captures that spirit.
This bio is hopefully helpful. I got a number of designs previously and they did not match my requests. Thank you for your creative input and considering my project.

Colors

Designer to choose colors to be used in the design.

Requirements
Must have
• Be approx 1 foot tall and 5 feet long, show boat name, and some sort of fun image of fish/s
Nice to have
• Us represented some way - mom and daughter depicted to look like fish or both of us catching fish
Should not have
• Only words

```html
<!DOCTYPE html>
<html lang="en">
<head>
<meta charset="utf-8">
<title>Keep Calm Cast On – Boat Graphic</title>
<link rel="stylesheet" href="https://fonts.googleapis.com/css2?family=Saira+Extra+Condensed:ital,wght@1,800&display=swap">
<style>
  :root {
    --bg-wine: #7e1139;
    --bg-wine-light: #8f1c47;
    --bg-wine-deep: #6a0a2e;
    --shadow-maroon: #4a0519;
    --letter-white: #ffffff;
    --letter-grey: #e2e0e3;
    --sticker-white: #ffffff;
    --badge-pink: #f0398f;
    --badge-purple: #6b3aa0;
    --badge-teal: #35c9c4;
    --badge-lime: #9be13a;
  }
  html, body {
    margin: 0;
    padding: 0;
    overflow: hidden;
    background: var(--bg-wine);
  }
  .boat-banner {
    position: relative;
    width: 1200px;
    height: 292px;
    overflow: hidden;
  }
  .banner-backdrop {
    position: absolute;
    inset: 0;
    background:
      radial-gradient(ellipse 420px 180px at 780px 250px, var(--bg-wine-deep), transparent 70%),
      radial-gradient(ellipse 500px 160px at 820px 40px, var(--bg-wine-light), transparent 70%),
      linear-gradient(180deg, var(--bg-wine-light) 0%, var(--bg-wine) 45%, var(--bg-wine-deep) 100%);
  }
  .fish-badge {
    position: absolute;
    left: 40px;
    top: 26px;
    width: 228px;
    height: 228px;
  }
  .boat-name {
    position: absolute;
    left: 280px;
    top: 70px;
    width: 900px;
    height: 140px;
  }
  .boat-name text {
    font-family: "Saira Extra Condensed", "Arial Narrow", sans-serif;
    font-weight: 800;
    font-style: italic;
    font-size: 150px;
    text-transform: uppercase;
  }
</style>
</head>
<body>
  <main class="boat-banner">
    <div class="banner-backdrop" role="img" aria-label="Faded photo of a fishing boat on rough water, tinted wine red"></div>

    <svg class="fish-badge" viewBox="0 0 228 228" aria-hidden="false">
      <defs>
        <linearGradient id="badgeArt" x1="0" y1="0" x2="0.4" y2="1">
          <stop offset="0" stop-color="var(--badge-pink)"/>
          <stop offset="0.45" stop-color="var(--badge-purple)"/>
          <stop offset="0.75" stop-color="var(--badge-teal)"/>
          <stop offset="1" stop-color="var(--badge-lime)"/>
        </linearGradient>
      </defs>
      <circle cx="114" cy="114" r="112" fill="var(--sticker-white)"/>
      <circle cx="114" cy="114" r="102" fill="url(#badgeArt)" role="img"
        aria-label="Illustration of a largemouth bass leaping from a splash in front of a neon sunset, mountains and pines"/>
    </svg>

    <svg class="boat-name" viewBox="0 0 900 140">
      <defs>
        <linearGradient id="letterFill" x1="0" y1="0" x2="0" y2="1">
          <stop offset="0" stop-color="var(--letter-white)"/>
          <stop offset="1" stop-color="var(--letter-grey)"/>
        </linearGradient>
      </defs>
      <text x="14" y="120" textLength="870" lengthAdjust="spacingAndGlyphs"
        fill="var(--shadow-maroon)" stroke="var(--shadow-maroon)" stroke-width="10" stroke-linejoin="round">Keep Calm Cast On</text>
      <text x="6" y="114" textLength="870" lengthAdjust="spacingAndGlyphs"
        fill="url(#letterFill)" stroke="var(--shadow-maroon)" stroke-width="8" stroke-linejoin="round"
        paint-order="stroke">Keep Calm Cast On</text>
    </svg>
  </main>
</body>
</html>
```